bright harbor crest Need a flyer ,ticket and banner design

childrent christmas party 2015
venue : korvan bay plaza tower 5 #04-615
singapore 047215

hi would like to get a design before sunday take note for the banner flyerthe theme will be (blue/gold)for ticket will attach sample here.here 3 sample

```html
<!DOCTYPE html>
<html lang="en">
<head>
<meta charset="utf-8">
<title>Christmas Party Tickets</title>
<link href="https://fonts.googleapis.com/css2?family=Bebas+Neue&display=swap" rel="stylesheet">
<style>
  :root {
    --gold-light: #ffe96a;
    --gold: #fcc419;
    --orange: #f4a10c;
    --orange-deep: #e98a05;
    --ink: #111111;
    --frame: #3a2a00;
    --glow: rgba(255, 255, 230, 0.45);
  }
  * { margin: 0; padding: 0; box-sizing: border-box; }
  html, body { width: 862px; height: 1200px; overflow: hidden; background: #ffffff; }
  body { font-family: "Bebas Neue", "Arial Narrow", sans-serif; color: var(--ink); }

  .sheet { position: relative; width: 862px; height: 1200px; }

  .ticket {
    position: relative;
    width: 862px;
    height: 300px;
    background: linear-gradient(100deg, var(--gold-light) 0%, var(--gold) 35%, var(--orange) 70%, var(--orange-deep) 100%);
    overflow: hidden;
  }
  .ticket::before {
    content: "";
    position: absolute;
    left: -60px; top: 40px;
    width: 760px; height: 220px;
    border-radius: 50%;
    background: radial-gradient(ellipse at 40% 50%, var(--glow), rgba(255,255,255,0) 70%);
  }

  .ticket-main {
    position: absolute;
    left: 22px; top: 16px;
    width: 650px; height: 264px;
    border: 1px solid var(--frame);
    text-align: center;
  }
  .laurel {
    position: absolute;
    left: 215px; top: 40px;
    width: 220px; height: 200px;
    border-radius: 50%;
    background: radial-gradient(ellipse, rgba(200, 140, 0, 0.18), rgba(200,140,0,0) 70%);
  }
  .brand {
    position: absolute;
    left: 0; right: 0; top: 10px;
    display: flex; align-items: center; justify-content: center; gap: 6px;
    font-size: 14px; letter-spacing: 1px;
  }
  .brand-mark { width: 12px; height: 12px; background: var(--ink); }
  .event-title {
    position: absolute; left: 0; right: 0; top: 70px;
    font-size: 36px; letter-spacing: 6px; line-height: 1;
  }
  .event-details {
    position: absolute; left: 0; right: 0; top: 112px;
    font-size: 21px; line-height: 23px;
  }
  .price {
    position: absolute; left: 0; right: 0; top: 182px;
    font-size: 64px; line-height: 1; letter-spacing: 1px;
  }

  .ticket-stub {
    position: absolute;
    left: 694px; top: 0;
    width: 168px; height: 300px;
    background: linear-gradient(160deg, var(--orange) 0%, var(--gold) 50%, var(--orange) 100%);
  }
  .stub-frame {
    position: absolute;
    left: 10px; top: 8px;
    width: 146px; height: 280px;
    border: 1px solid var(--frame);
  }
  .stub-text {
    position: absolute;
    left: 50%; top: 50%;
    width: 250px;
    transform: translate(-50%, -50%) rotate(-90deg);
    text-align: center;
  }
  .stub-title { font-size: 33px; letter-spacing: 6px; line-height: 36px; }
  .stub-date { font-size: 19px; line-height: 22px; margin-top: 4px; }
</style>
</head>
<body>
<main class="sheet">
  <section class="ticket">
    <div class="ticket-main">
      <div class="laurel" role="img" aria-label="Faint golden laurel wreath decoration"></div>
      <div class="brand"><span class="brand-mark"></span>BRIGHT HARBOR CREST</div>
      <h1 class="event-title">CHRISTMAS PARTY</h1>
      <p class="event-details">19TH DEC 2015<br>1400HR TO 1800HR<br>KORVAN BAY PLAZA TOWER 5 #04-615</p>
      <p class="price">1 CHILL 1 ADULT $ 22</p>
    </div>
    <div class="ticket-stub"><div class="stub-frame"></div>
      <div class="stub-text"><div class="stub-title">CHRISTMAS<br>PARTY</div><div class="stub-date">19TH DEC 2015<br>1400HR TO 1800HR</div></div>
    </div>
  </section>
  <section class="ticket">
    <div class="ticket-main">
      <div class="laurel" role="img" aria-label="Faint golden laurel wreath decoration"></div>
      <div class="brand"><span class="brand-mark"></span>BRIGHT HARBOR CREST</div>
      <h1 class="event-title">CHRISTMAS PARTY</h1>
      <p class="event-details">19TH DEC 2015<br>1400HR TO 1800HR<br>KORVAN BAY PLAZA TOWER 5 #04-615</p>
      <p class="price">1 CHILL 1 ADULT $ 22</p>
    </div>
    <div class="ticket-stub"><div class="stub-frame"></div>
      <div class="stub-text"><div class="stub-title">CHRISTMAS<br>PARTY</div><div class="stub-date">19TH DEC 2015<br>1400HR TO 1800HR</div></div>
    </div>
  </section>
  <section class="ticket">
    <div class="ticket-main">
      <div class="laurel" role="img" aria-label="Faint golden laurel wreath decoration"></div>
      <div class="brand"><span class="brand-mark"></span>BRIGHT HARBOR CREST</div>
      <h1 class="event-title">CHRISTMAS PARTY</h1>
      <p class="event-details">19TH DEC 2015<br>1400HR TO 1800HR<br>KORVAN BAY PLAZA TOWER 5 #04-615</p>
      <p class="price">1 CHILL 1 ADULT $ 22</p>
    </div>
    <div class="ticket-stub"><div class="stub-frame"></div>
      <div class="stub-text"><div class="stub-title">CHRISTMAS<br>PARTY</div><div class="stub-date">19TH DEC 2015<br>1400HR TO 1800HR</div></div>
    </div>
  </section>
  <section class="ticket">
    <div class="ticket-main">
      <div class="laurel" role="img" aria-label="Faint golden laurel wreath decoration"></div>
      <div class="brand"><span class="brand-mark"></span>BRIGHT HARBOR CREST</div>
      <h1 class="event-title">CHRISTMAS PARTY</h1>
      <p class="event-details">19TH DEC 2015<br>1400HR TO 1800HR<br>KORVAN BAY PLAZA TOWER 5 #04-615</p>
      <p class="price">1 CHILL 1 ADULT $ 22</p>
    </div>
    <div class="ticket-stub"><div class="stub-frame"></div>
      <div class="stub-text"><div class="stub-title">CHRISTMAS<br>PARTY</div><div class="stub-date">19TH DEC 2015<br>1400HR TO 1800HR</div></div>
    </div>
  </section>
</main>
</body>
</html>
```